Redesign the content on our home page

Thanks for your designs thus far.

There have been a few requests for feedback, so I have mocked up another layout. I am happy with everything except the 6 boxes in the green square. This is the piece I need the perfect design for.
- What the boxes look like
- Icons to be used
- Colours
- etc

__________________________________________________________________

We have the basic layout for our homepage, the header and footer are done. Please see attached (Homepage)

Only design in PSD etc needed, no coding. Also, header and footer not needed either, only formatting and graphic design of home page content. See eps file for the information.

I need more information added to the homepage and displayed in an organised way and designed so it presents well.

Our slogan is "Travel Insurance made simple". Therefore the design needs to represent this by being a simple, clear and clean layout of information. Website visitors need to be able to access and digest the information fast and this is reliant on the design of the information.

Attached is a mock up with all of the information.

Please ask and questions you need to help with the design.

Project Deadline Extended Reason: Deadline has been extended to provide further clarification for the required design.I need the 6 boxes inside the green outline designed. The design of the 6 boxes should be simple and follow the pages design and be simple in appearance. Thanks for your designs thus far. Added Thursday, October 8, 2015

Target Market(s)

Mostly female, any age.

Industry/Entity Type

Travel

Number of Pages Required

1 page

Font styles to use
Other font styles liked:
• MetaPro

Colors
f37122
33a6d7
33b8a4
dbdbdb
606060

Requirements
Must have
• - Follow home page look and feel
• - Simple design
• - Fast for a visitor to digest the information
Nice to have
• Simple design. Webpage is responsive so elements should look good when scaled for mobile.
Should not have
• No new colours to be introduced then what is in the design already or selected below.
• No new fonts.

```html
<!DOCTYPE html>
<html lang="en">
<head>
<meta charset="utf-8">
<title>Tripwise – Travel Insurance Made Simple</title>
<link href="https://fonts.googleapis.com/css2?family=Source+Sans+3:wght@400;600;700&display=swap" rel="stylesheet">
<style>
:root{
  --orange:#f37122;
  --orange-dark:#e0621a;
  --blue:#33a6d7;
  --teal:#33b8a4;
  --light:#dbdbdb;
  --pale:#f2f2f2;
  --dark:#606060;
  --white:#ffffff;
  --red:#d9432b;
}
*{box-sizing:border-box;margin:0;padding:0}
html,body{width:1200px;height:2364px;overflow:hidden}
body{font-family:"Source Sans 3",Arial,sans-serif;color:var(--dark);background:var(--white);font-size:14px;line-height:1.45}
.page{position:relative;width:1200px;height:2364px}

/* header */
.site-header{height:70px;display:flex;align-items:center;justify-content:space-between;padding:0 60px;background:var(--white);border-bottom:3px solid var(--orange)}
.brand{display:flex;align-items:center;gap:8px;font-weight:700;font-size:26px;color:var(--orange)}
.brand-dot{width:14px;height:14px;border-radius:50%;background:var(--orange)}
.brand small{display:block;font-size:10px;color:var(--dark);font-weight:400;margin-top:-4px}
.top-nav{display:flex;gap:22px;align-items:center;font-size:14px;color:var(--orange)}
.top-nav .phone{font-weight:700;font-size:16px}

/* hero */
.hero{position:relative;height:440px;background:var(--orange);overflow:hidden}
.hero-figure{position:absolute;left:150px;top:70px;width:150px;height:260px;background:linear-gradient(#d85c1a,#b94b15);border-radius:12px}
.hero-luggage{position:absolute;right:150px;top:210px;width:190px;height:110px;background:linear-gradient(#d85c1a,#c2511a);border-radius:8px}
.hero-form{position:absolute;left:0;right:0;top:80px;text-align:center;color:var(--white)}
.hero-line{display:flex;justify-content:center;align-items:center;gap:14px;font-size:48px;font-weight:600;margin-bottom:16px}
.field{background:var(--white);border-radius:6px;height:46px;display:inline-flex;align-items:center;padding:0 12px;color:var(--dark);font-size:15px;gap:8px}
.field.destination{width:210px;justify-content:space-between}
.field.date{width:86px;flex-direction:column;justify-content:center;padding:0;overflow:hidden}
.field.date b{display:block;width:100%;background:var(--blue);color:var(--white);font-size:11px;text-align:center;line-height:16px}
.field.date span{font-size:18px;line-height:28px;font-weight:700}
.help{width:22px;height:22px;border-radius:50%;background:var(--white);color:var(--orange);font-size:13px;font-weight:700;display:inline-flex;align-items:center;justify-content:center}
.btn{display:inline-block;background:var(--orange-dark);color:var(--white);border:2px solid var(--white);border-radius:20px;padding:8px 26px;font-size:14px;font-weight:600}
.underwriter{margin-top:18px;font-size:14px;font-weight:700;color:var(--white)}
.hero-curve{position:absolute;left:0;bottom:0;width:1200px;height:90px}

/* simple */
.section-title{color:var(--orange);font-size:24px;font-weight:700;letter-spacing:1px;text-align:center;text-transform:uppercase}
.section-lead{text-align:center;font-size:13px;max-width:600px;margin:6px auto 0}
.simple{padding:30px 0 40px;position:relative}
.simple-grid{display:flex;justify-content:center;gap:40px;margin-top:28px}
.simple-item{width:170px;text-align:center}
.icon-circle{width:66px;height:66px;border-radius:50%;background:var(--orange);margin:0 auto 12px;display:flex;align-items:center;justify-content:center}
.simple-item h3{font-size:15px;color:var(--dark);font-weight:700;line-height:1.2;margin-bottom:6px}
.simple-item p{font-size:12px}
.arrow{position:absolute;top:150px;font-size:30px;color:var(--dark)}
.arrow.prev{left:200px}.arrow.next{right:200px}

/* award */
.award{background:var(--orange);height:175px;color:var(--white);text-align:center;padding-top:30px}
.award .section-title{color:var(--white)}
.award-row{display:flex;justify-content:center;align-items:center;gap:30px;margin-top:26px}
.award-name{font-size:34px;font-weight:700}
.award-text{text-align:left;font-size:13px}

/* confidence */
.confidence{padding:36px 0 30px}
.badges{display:flex;justify-content:center;gap:44px;margin-top:26px}
.badge{width:150px;text-align:center}
.badge-shape{width:58px;height:58px;border-radius:50%;border:4px solid var(--red);margin:0 auto 10px;background:var(--white)}
.badge p{font-size:12px}

/* strip */
.strip{background:var(--orange);color:var(--white);text-align:center;font-size:13px;height:40px;line-height:40px}

/* features */
.features{background:var(--pale);height:220px;display:flex;justify-content:center;gap:110px;padding-top:40px}
.feature{width:230px;text-align:center}
.feature svg{display:block;margin:0 auto 10px}
.feature h4{color:var(--orange);font-size:15px;font-weight:700;margin-bottom:4px}
.feature p{font-size:12px}
.skyline{height:80px;background:linear-gradient(var(--pale),#cfcfcf)}

/* seen on */
.seen{padding:24px 0 30px;text-align:center}
.seen h5{font-size:15px;color:var(--dark);font-weight:600;margin-bottom:14px}
.logos{display:flex;justify-content:center;gap:30px}
.logo-box{width:100px;height:50px;background:var(--white);border:1px solid var(--light);border-radius:3px}

/* footer */
.footer-top{background:var(--pale);height:200px;display:flex;justify-content:center;gap:40px;padding-top:30px}
.footer-brand{width:190px}
.footer-brand .brand{font-size:30px}
.footer-brand p{font-size:13px;font-weight:700;margin-top:10px}
.newsletter{width:240px;background:var(--orange);color:var(--white);border-radius:4px;padding:14px}
.newsletter h6{font-size:15px}
.newsletter p{font-size:11px;margin-bottom:8px}
.newsletter .input{height:24px;background:var(--white);border-radius:3px;margin-bottom:6px}
.newsletter .signup{display:block;width:90px;margin:6px auto 0;text-align:center;background:var(--white);color:var(--orange);border-radius:3px;font-size:12px;font-weight:700;padding:3px 0}
.contact-col{width:180px;font-size:12px}
.contact-col h6{font-size:15px;color:var(--orange)}
.contact-col a{color:var(--blue);text-decoration:none;display:block}
.footer-links{background:var(--white);height:300px;display:flex;justify-content:center;gap:110px;padding-top:40px}
.link-col h6{font-size:14px;color:var(--orange);margin-bottom:6px}
.link-col li{list-style:none;font-size:12px;line-height:1.8}
.legal{padding:0 180px;font-size:10px;text-align:center;color:#8a8a8a;line-height:1.5}
</style>
</head>
<body>
<div class="page">

<header class="site-header">
  <div class="brand"><span class="brand-dot"></span><div>Tripwise<small>Travel insurance made simple</small></div></div>
  <nav class="top-nav"><span>Travel Insurance</span><span>Make a claim</span><span>Your Policy</span><span>FAQ</span><span>Emergency</span><span class="phone">1300 555 018</span></nav>
</header>

<section class="hero">
  <div class="hero-figure" role="img" aria-label="Illustrated traveller waving"></div>
  <div class="hero-luggage" role="img" aria-label="Illustrated suitcases"></div>
  <div class="hero-form">
    <div class="hero-line">I'm travelling to <span class="field destination">Select <span>▾</span></span><span class="help">?</span></div>
    <div class="hero-line">from <span class="field date"><b>Sep</b><span>10</span></span> till <span class="field date"><b>Month</b><span>▾</span></span><span class="help">?</span></div>
    <span class="btn">I'm travelling multiple times in the year</span>
    <div class="underwriter">Northgate</div>
  </div>
  <svg class="hero-curve" viewBox="0 0 1200 90" preserveAspectRatio="none"><path d="M0 90 L0 55 Q600 -20 1200 55 L1200 90 Z" fill="#fff"/></svg>
</section>

<section class="simple">
  <h2 class="section-title">Travel Insurance Made Simple</h2>
  <p class="section-lead">We take out the hassle from choosing travel cover so you can focus on your trip.</p>
  <span class="arrow prev">‹</span><span class="arrow next">›</span>
  <div class="simple-grid">
    <div class="simple-item"><div class="icon-circle"><svg width="30" height="30" viewBox="0 0 30 30"><path d="M5 16 L12 23 L25 8" stroke="#fff" stroke-width="4" fill="none"/></svg></div><h3>Fast &amp; Simple Instant Quotes</h3><p>Get a price for your trip in seconds with only a few easy details needed.</p></div>
    <div class="simple-item"><div class="icon-circle"><svg width="30" height="30" viewBox="0 0 30 30"><path d="M15 4 V26 M4 15 H26" stroke="#fff" stroke-width="5"/></svg></div><h3>24 Hour Medical Assistance</h3><p>Help is always a phone call away wherever you are in the world.</p></div>
    <div class="simple-item"><div class="icon-circle"><svg width="30" height="30" viewBox="0 0 30 30"><path d="M3 14 L27 4 L20 27 L14 17 Z" fill="#fff"/></svg></div><h3>A Simple PDS Policy</h3><p>Clear wording that tells you what is covered without any fine print.</p></div>
    <div class="simple-item"><div class="icon-circle"><svg width="30" height="30" viewBox="0 0 30 30"><text x="15" y="23" font-size="24" font-weight="700" text-anchor="middle" fill="#fff" font-family="Source Sans 3, sans-serif">$</text></svg></div><h3>Fast &amp; Secure Purchase</h3><p>Buy online securely and receive your policy by email straight away.</p></div>
  </div>
</section>

<section class="award">
  <h2 class="section-title">Award Winning Travel Insurance</h2>
  <div class="award-row">
    <span class="award-name">Ratewise</span>
    <div class="award-text">Rated best value travel insurance 2015<br>Rated best value travel insurance 2014</div>
  </div>
</section>

<section class="confidence">
  <h2 class="section-title">Travel With Confidence</h2>
  <p class="section-lead">When you purchase a travel policy with us, you can rest assured that you are covered from the moment you buy, right up until you return home.</p>
  <div class="badges">
    <div class="badge"><div class="badge-shape"></div><p>Cover for cancellation and lost deposits before you leave.</p></div>
    <div class="badge"><div class="badge-shape"></div><p>Overseas medical expenses covered with no upper limit.</p></div>
    <div class="badge"><div class="badge-shape"></div><p>Luggage and personal items protected throughout your trip.</p></div>
    <div class="badge"><div class="badge-shape"></div><p>Personal liability cover included on every single policy.</p></div>
  </div>
</section>

<div class="strip">Free cover for dependent children on all our policies when travelling with you.</div>

<section class="features">
  <div class="feature"><svg width="34" height="34" viewBox="0 0 34 34"><path d="M6 6 L28 28 M28 6 L6 28" stroke="#606060" stroke-width="5"/></svg><h4>Cancel Anytime</h4><p>Change your mind before you travel and receive a full refund within the cooling off period.</p></div>
  <div class="feature"><svg width="34" height="34" viewBox="0 0 34 34"><path d="M17 32 C9 20 7 16 7 12 A10 10 0 0 1 27 12 C27 16 25 20 17 32 Z" fill="#606060"/><circle cx="17" cy="12" r="4" fill="#f2f2f2"/></svg><h4>Travel Guide</h4><p>Helpful tips and advice for every destination so you can plan ahead with ease.</p></div>
  <div class="feature"><svg width="34" height="34" viewBox="0 0 34 34"><path d="M3 7 L12 4 L22 8 L31 5 V27 L22 30 L12 26 L3 29 Z" fill="none" stroke="#606060" stroke-width="3"/><path d="M12 4 V26 M22 8 V30" stroke="#606060" stroke-width="3"/></svg><h4>Travel Blogs</h4><p>Stories and ideas from fellow travellers to inspire your next trip away.</p></div>
</section>
<div class="skyline" role="img" aria-label="Grey city skyline silhouette"></div>

<section class="seen">
  <h5>As Seen On</h5>
  <div class="logos"><span class="logo-box"></span><span class="logo-box"></span><span class="logo-box"></span><span class="logo-box"></span><span class="logo-box"></span><span class="logo-box"></span></div>
</section>

<section class="footer-top">
  <div class="footer-brand"><div class="brand"><span class="brand-dot"></span>Tripwise</div><p>Northgate</p></div>
  <div class="newsletter"><h6>Want travel tips &amp; freebies?</h6><p>Join our newsletter</p><div class="input"></div><div class="input"></div><span class="signup">Sign up</span></div>
  <div class="contact-col"><h6>Need a hand?</h6><p>Contact us</p><p>1300 555 018</p><a>hello@tripwise.example</a><a>claims@tripwise.example</a></div>
  <div class="contact-col"><h6>Making a claim?</h6><p>Visit our claims page</p><a>Start your claim online</a></div>
</section>

<section class="footer-links">
  <div class="link-col"><h6>Cover</h6><ul><li>Single Trip Cover</li><li>Annual Multi Trip</li><li>Seniors Cover</li><li>Family Cover</li><li>Cruise Cover</li><li>Ski Cover</li></ul></div>
  <div class="link-col"><h6>Support</h6><ul><li>Make a Claim</li><li>Emergency Help</li><li>Policy Wording</li><li>FAQ</li><li>Contact Us</li></ul></div>
  <div class="link-col"><h6>About</h6><ul><li>About Us</li><li>Blog</li><li>Privacy Policy</li><li>Terms of Use</li><li>Careers</li></ul></div>
</section>

<p class="legal">Travel insurance is issued by our underwriting partner. Any advice given is general only and does not take into account your objectives, financial situation or needs. Please read the product disclosure statement before deciding to buy. Cover is subject to the terms, conditions, limits and exclusions of the policy. © 2015 Tripwise. All rights reserved.</p>

</div>
</body>
</html>
```